Kestrel Summit 2019 Enemies of the End-Times Church Flyer

We want a church conference flyer designed. We are looking for a professional, yet catchy design that uses our brand colors and logo creatively while communicating key information of the event effectively. <br/>The flyer must include all of the following:<br/>Title: Kestrel Summit 2019<br/>Topic: The Enemies of The End-Times Church <br/>Subtitles: <br/> -How the antichrist raises an army by social behavior engineering. <br/>-How the architects of modern social constructs escaped the church's radar. <br/>-The Holy Spirit's end-times agenda:<br/> The Knock-Out Punch!<br/>Speaker: Prophet Marcus Toliver <br/>Dates/time: December 27, 28 & 29 at 6pm<br/>Location: Halvorn Community Center <br/> 241 Pellham Street <br/> Portland, ME 04102<br/>Contact info: phone: 207-555-0148 <br/>email: contact@brookmeadow.example <br/> www.vutel.example<br/>*The flyer must also include a picture of the speaker and our Vutel logo <br/>Thanks, we look forward to seeing what you come up with!

Colors

Designer to choose colors to be used in the design.

Requirements
Must have
• The flyer must include all of the following:
• Title: Kestrel Summit 2019
• Topic: The Enemies of The End-Times Church
• Subtitles:
• -How the antichrist raises an army by social behavior engineering.
• -How the architects of modern social constructs escaped the church's radar.
• -The Holy Spirit's end-times agenda:
• The Knock-Out Punch!
• Speaker: Prophet Marcus Toliver
• Dates/time: December 27, 28 & 29 at 6pm
• Location: Halvorn Community Center
• 241 Pellham Street
• Portland, ME 04102
• Contact info: phone: 207-555-0148
• email: contact@brookmeadow.example
• www.vutel.example
• *The flyer must also include a picture of the speaker and our Vutel logo
Should not have
• Pictures of crosses or church buildings

```html
<!DOCTYPE html>
<html lang="en">
<head>
<meta charset="utf-8">
<title>Kestrel Summit 2019 — Flyer</title>
<link href="https://fonts.googleapis.com/css2?family=Poppins:wght@600&family=Barlow+Condensed:wght@500;600&family=Advent+Pro:wght@400;500&family=Comfortaa:wght@600&display=swap" rel="stylesheet">
<style>
  :root {
    --backdrop: #E27302;
    --cream: #FFFDF0;
    --cream-deep: #F6EFD3;
    --red: #C41E33;
    --navy: #0E3558;
    --orange: #F0883A;
    --amber: #F7A92E;
  }
  * { margin: 0; padding: 0; box-sizing: border-box; }
  html, body { width: 1200px; height: 1200px; overflow: hidden; }
  body { background: var(--backdrop); position: relative; }

  .flyer {
    position: absolute; left: 229px; top: 75px;
    width: 741px; height: 1048px; overflow: hidden;
    background: radial-gradient(ellipse at 45% 40%, var(--cream) 0%, var(--cream-deep) 75%, #ECE9E0 100%);
  }
  .flyer-art { position: absolute; inset: 0; width: 100%; height: 100%; }

  .brand {
    position: absolute; left: 0; width: 741px; top: 118px;
    display: flex; justify-content: center; align-items: center; gap: 10px;
    font: 600 48px/1 'Poppins', sans-serif; color: var(--navy); letter-spacing: 1px;
  }
  .brand-dot { width: 16px; height: 16px; border-radius: 50%; background: var(--orange); }

  .title {
    position: absolute; left: 69px;
    font: 600 78px/1 'Poppins', sans-serif; color: var(--red); letter-spacing: 2px;
  }
  .title--line1 { top: 172px; }
  .title--line2 { top: 242px; }
  .title--year  { top: 320px; }

  .topic {
    position: absolute; left: 69px; top: 405px;
    font: 500 44px/1 'Barlow Condensed', sans-serif; color: var(--navy);
  }

  .talks {
    position: absolute; left: 76px; top: 466px; list-style: none;
    font: 500 17.5px/24px 'Barlow Condensed', sans-serif; color: var(--red);
  }
  .talks li { position: relative; padding-left: 14px; }
  .talks li::before {
    content: ""; position: absolute; left: 0; top: 8px;
    border-left: 6px solid var(--red); border-top: 4px solid transparent; border-bottom: 4px solid transparent;
  }

  .details { position: absolute; left: 40px; width: 400px; text-align: center; }
  .pin { position: absolute; left: 226px; top: 606px; }
  .venue { top: 640px; font: 600 27px/1 'Barlow Condensed', sans-serif; color: var(--red); }
  .address { top: 674px; font: 600 22px/1 'Barlow Condensed', sans-serif; color: var(--navy); }

  .speaker-rule { position: absolute; left: 79px; width: 308px; height: 1.5px; background: var(--red); }
  .speaker-rule--top { top: 736px; }
  .speaker-rule--bottom { top: 767px; }
  .speaker { top: 740px; font: 400 23px/1 'Advent Pro', sans-serif; color: var(--navy); letter-spacing: 0.5px; }

  .label { font: 500 21px/1 'Advent Pro', sans-serif; color: var(--navy); letter-spacing: 0.5px; }
  .label--dates { top: 783px; }
  .label--time { top: 843px; }
  .dates { top: 801px; font: 600 40px/1 'Barlow Condensed', sans-serif; color: var(--red); }
  .time { top: 862px; font: 600 40px/1 'Barlow Condensed', sans-serif; color: var(--navy); }

  .phone-icon { position: absolute; left: 101px; top: 941px; }
  .phone {
    position: absolute; left: 47px; width: 160px; top: 985px; text-align: center;
    font: 600 23px/1 'Barlow Condensed', sans-serif; color: var(--red);
  }
  .web-contact {
    position: absolute; right: 289px; text-align: right;
    font: 600 14.5px/1 'Comfortaa', sans-serif; color: var(--red); letter-spacing: 0.3px;
  }
  .web-contact--email { top: 974px; }
  .web-contact--site { top: 993px; }
  .contact-icon { position: absolute; left: 462px; }
  .contact-icon--email { top: 974px; }
  .contact-icon--site { top: 993px; }
</style>
</head>
<body>
  <main class="flyer">
    <svg class="flyer-art" viewBox="0 0 926 1310" preserveAspectRatio="none" aria-hidden="false">
      <defs>
        <radialGradient id="leafGlow" cx="0.2" cy="0.15" r="0.6">
          <stop offset="0" stop-color="#F6C948" stop-opacity="0.85"/>
          <stop offset="0.5" stop-color="#F8DC7A" stop-opacity="0.45"/>
          <stop offset="1" stop-color="#FFF6D8" stop-opacity="0"/>
        </radialGradient>
        <linearGradient id="flameFill" x1="0" y1="0" x2="1" y2="0">
          <stop offset="0" stop-color="#EE7A38"/>
          <stop offset="1" stop-color="#F7A92E"/>
        </linearGradient>
        <linearGradient id="innerGlow" x1="0" y1="0" x2="1" y2="1">
          <stop offset="0" stop-color="#E8503A"/>
          <stop offset="1" stop-color="#F39A34"/>
        </linearGradient>
        <linearGradient id="portraitTone" x1="0" y1="0" x2="0" y2="1">
          <stop offset="0" stop-color="#5A4A44"/>
          <stop offset="0.5" stop-color="#8E2A2E"/>
          <stop offset="1" stop-color="#33363D"/>
        </linearGradient>
      </defs>

      <rect role="img" aria-label="Autumn maple leaves scattered across the top left corner" x="0" y="0" width="560" height="420" fill="url(#leafGlow)"/>
      <ellipse role="img" aria-label="Autumn leaves in the top right corner" cx="820" cy="20" rx="110" ry="50" fill="#F4B640" opacity="0.45"/>

      <path class="flame" fill="url(#flameFill)"
        d="M829,76 C750,140 730,240 780,330 C840,430 875,530 860,610 C845,690 790,720 740,718 C700,716 680,690 664,646 C560,720 510,900 560,1060 C600,1180 690,1270 770,1310 L926,1310 L926,281 C870,250 835,160 829,76 Z"/>
      <path class="flame-inner" fill="url(#innerGlow)"
        d="M664,646 C600,760 570,900 600,1040 C630,1160 700,1250 800,1310 L926,1310 L926,700 C860,720 760,720 664,646 Z"/>
      <path class="flame-band" fill="var(--red)"
        d="M664,646 C540,740 490,920 540,1070 C580,1180 670,1260 770,1310 L812,1310 C700,1240 620,1150 595,1040 C565,900 590,760 664,646 Z"/>

      <path role="img" aria-label="Portrait photo of speaker Prophet Marcus Toliver"
        fill="url(#portraitTone)"
        d="M650,840 C660,760 700,716 760,716 C830,716 870,770 880,840 C900,900 926,940 926,960 L926,1310 L780,1310 C700,1250 630,1160 605,1050 C595,990 620,930 650,840 Z"/>
    </svg>

    <div class="brand"><span class="brand-dot"></span>Vutel</div>

    <h1>
      <span class="title title--line1">KESTREL</span>
      <span class="title title--line2">SUMMIT</span>
      <span class="title title--year">2019</span>
    </h1>

    <h2 class="topic">The Enemies of The End-Times Church</h2>

    <ul class="talks">
      <li>How the antichrist raises an army by social behavior engineering.</li>
      <li>How the architects of modern social constructs escaped the church's radar.</li>
      <li>The Holy Spirit's end-times agenda:</li>
      <li>The Knock-Out Punch!</li>
    </ul>

    <svg class="pin" width="34" height="42" viewBox="0 0 34 42" aria-hidden="true">
      <path d="M17 3 C10 3 6 8 6 14 C6 22 17 31 17 31 C17 31 28 22 28 14 C28 8 24 3 17 3 Z" fill="none" stroke="var(--red)" stroke-width="3"/>
      <circle cx="17" cy="14" r="4" fill="var(--red)"/>
      <path d="M9 30 L3 39 L31 39 L25 30" fill="none" stroke="var(--red)" stroke-width="2.5"/>
    </svg>
    <p class="details venue">Halvorn Community Center</p>
    <p class="details address">241 Pellham Street | Portland, ME 04102</p>

    <div class="speaker-rule speaker-rule--top"></div>
    <p class="details speaker" style="left:33px">Speaker: Prophet Marcus Toliver</p>
    <div class="speaker-rule speaker-rule--bottom"></div>

    <p class="details label label--dates">Dates</p>
    <p class="details dates">December 27, 28 &amp; 29</p>
    <p class="details label label--time">Time</p>
    <p class="details time">6pm</p>

    <svg class="phone-icon" width="40" height="40" viewBox="0 0 40 40" aria-hidden="true">
      <circle cx="20" cy="20" r="18" fill="none" stroke="var(--red)" stroke-width="2"/>
      <path d="M13 11 L17 10 L19 16 L16.5 18 C18 21 19.5 22.5 22 23.5 L24 21 L30 23 L29 27 C22 29 11 18 13 11 Z" fill="none" stroke="var(--red)" stroke-width="1.8" stroke-linejoin="round"/>
    </svg>
    <p class="phone">207-555-0148</p>

    <p class="web-contact web-contact--email">contact@brookmeadow.example</p>
    <p class="web-contact web-contact--site">www.vutel.example</p>
    <svg class="contact-icon contact-icon--email" width="16" height="13" viewBox="0 0 16 13" aria-hidden="true">
      <rect x="1" y="1.5" width="14" height="10" fill="none" stroke="var(--red)" stroke-width="1.2"/>
      <path d="M1 1.5 L8 7 L15 1.5" fill="none" stroke="var(--red)" stroke-width="1.2"/>
    </svg>
    <svg class="contact-icon contact-icon--site" width="15" height="15" viewBox="0 0 16 16" aria-hidden="true">
      <circle cx="8" cy="8" r="6.5" fill="none" stroke="var(--red)" stroke-width="1.2"/>
      <ellipse cx="8" cy="8" rx="3" ry="6.5" fill="none" stroke="var(--red)" stroke-width="1.1"/>
      <path d="M1.5 8 H14.5 M2.5 4.8 H13.5 M2.5 11.2 H13.5" stroke="var(--red)" stroke-width="1.1"/>
    </svg>
  </main>
</body>
</html>
```